※本のタイトルや内容・紹介文などの書籍情報は、 ご参考資料をPDFとして添付させていただきますので、 ご確認いただければと思います。 ▼納品ファイル形式 -------------------------------------------------------------- 1.縦2,600px、横1,625px のjpegファイル 及び 2.jpeg画像の作成元データとなったaiファイルもしくはpsdファイル を納品してください。 -------------------------------------------------------------- ※注意点・禁止事項 ・他で登録されているデザインや商標の転用など、他社の知的財産権を侵すこと ・他のクライアントへ既に提案した内容の転用など ※その他コメント ・デザイン案の数は問いません。 ・クオリティは、市販の書籍並で結構です。 ・良いデザインを提案してくださった方には、このお仕事以外にも継続的にご依頼させていただきます。 ・その他、デザイン作成について疑問等がありましたら、お気軽にご相談下さい。 たくさんのご応募をお待ちしております。 |
この度は、たくさんのご提案をいただきまして、
誠にありがとうございました。
多くの素晴らしいデザインをご提案していただき、
本当に感謝しております。
今回、ご選考の結果、
kqb587w9さんのデザインを採用させていただきました。
※本案件に関しましては、書籍のイメージに一番合ったものが、
kqb587w9さんの表紙デザインだったため、
今回は、kqb587w9さんのご提案を選定させていただきました。
本当に、ありがとうございました。
また、今回は残念ながら、ご採用に至らなかった方も、
この度はお忙しいところ、本案件にご参加いただきまして、
今後も、継続的にお仕事をご発注させていただきますので、
また宜しければご参加いただければ幸いです。
以上、今後とも、何卒よろしくお願いいたします。

```html
<!DOCTYPE html>
<html lang="ja">
<head>
<meta charset="UTF-8">
<title>白い花 ＊ 夏が来るまえに</title>
<link rel="stylesheet" href="https://fonts.googleapis.com/css2?family=Shippori+Mincho:wght@500;700;800&display=swap">
<style>
  :root {
    --mist-light: #f3edd9;
    --mist-mid: #d9cca8;
    --mist-dark: #6f6446;
    --tree-shade: #3e3a2a;
    --field-green: #5e6238;
    --title-red: #c8102e;
    --subtitle-red: #8a1020;
    --author-ink: #4a3a2a;
    --band-maroon: #5a0d14;
    --copy-white: #ffffff;
  }
  html, body {
    margin: 0;
    padding: 0;
    width: 749px;
    height: 1200px;
    overflow: hidden;
    background: #ffffff;
  }
  .cover {
    position: relative;
    width: 749px;
    height: 1200px;
    overflow: hidden;
    font-family: "Shippori Mincho", serif;
    background: var(--band-maroon);
  }
  .cover-scene {
    position: absolute;
    left: 0;
    top: 0;
    width: 749px;
    height: 850px;
    background:
      linear-gradient(to right, var(--tree-shade) 0%, rgba(62,58,42,0.55) 18%, rgba(0,0,0,0) 40%),
      linear-gradient(to bottom, rgba(0,0,0,0) 68%, var(--field-green) 84%, #4a4a2a 100%),
      radial-gradient(ellipse 75% 60% at 68% 40%, var(--mist-light) 0%, var(--mist-mid) 55%, var(--mist-dark) 100%);
  }
  .title-block {
    position: absolute;
    left: 0;
    right: 0;
    text-align: center;
    margin: 0;
    line-height: 1;
  }
  .title-main {
    top: 362px;
    left: 40px;
    font-size: 100px;
    font-weight: 800;
    color: var(--title-red);
    letter-spacing: 4px;
  }
  .title-mark {
    top: 488px;
    left: 40px;
    font-size: 60px;
    font-weight: 700;
    color: var(--title-red);
  }
  .title-sub {
    top: 542px;
    left: 40px;
    font-size: 48px;
    font-weight: 700;
    color: var(--subtitle-red);
    letter-spacing: 1px;
  }
  .author {
    position: absolute;
    right: 24px;
    top: 678px;
    margin: 0;
    font-size: 56px;
    font-weight: 800;
    color: var(--author-ink);
    letter-spacing: 6px;
    line-height: 1;
  }
  .synopsis {
    position: absolute;
    left: 32px;
    top: 858px;
    margin: 0;
    color: var(--copy-white);
    font-weight: 700;
  }
  .synopsis-lead {
    margin: 0;
    font-size: 34px;
    line-height: 48px;
    letter-spacing: 0.5px;
  }
  .synopsis-tagline {
    margin: 10px 0 0;
    font-size: 40px;
    line-height: 58px;
  }
</style>
</head>
<body>
  <main class="cover">
    <div class="cover-scene" role="img" aria-label="霧に包まれた野原の小道、左に大きな木、その下に立つ二人の子どもの後ろ姿の写真"></div>

    <h1 class="title-block title-main">白い花</h1>
    <div class="title-block title-mark" aria-hidden="true">＊</div>
    <h2 class="title-block title-sub">夏が来るまえに</h2>

    <p class="author">森川 渉</p>

    <section class="synopsis">
      <p class="synopsis-lead">野原で出会った印象的なひとりの少女。<br>僕はその少女の非常にさびしげな顔付を<br>少々不思議に思って、じっとみつめていた。</p>
      <p class="synopsis-tagline">終戦後の貧困、中高生の苦悩・純愛を<br>心に伝える物語 ―</p>
    </section>
  </main>
</body>
</html>
```